Business Card Design for Mortgage Broking Business

We need to redesign the business card. Mortgage broking business, doing home loan and commercial loans, existing logo, also QLPN member logo. design style needs to be simple, professional, elegant.

once final, need to setup for a team of different names and contact details.

Industry/Entity Type

Loan

Contact Information for Business Card

Name; Mobile; Email; Address; Tel; Fax; Australian Credit Licence: 782316

```html
<!DOCTYPE html>
<html lang="en">
<head>
<meta charset="utf-8">
<title>Business Card – Front and Back</title>
<link rel="stylesheet" href="https://fonts.googleapis.com/css2?family=Exo+2:wght@400;600;700&display=swap">
<style>
  :root {
    --bg: #e4e4e4;
    --card-white: #ffffff;
    --brand-blue: #0f4c86;
    --brand-green: #5cbf5a;
    --ink: #2e2e2e;
    --ink-soft: #555555;
    --divider: rgba(255,255,255,0.22);
    --shadow: 0 18px 40px rgba(0,0,0,0.22);
  }
  * { box-sizing: border-box; margin: 0; padding: 0; }
  html, body { width: 1200px; height: 949px; overflow: hidden; }
  body {
    background: var(--bg);
    font-family: "Exo 2", sans-serif;
    color: var(--ink);
    position: relative;
  }
  .card {
    position: absolute;
    top: 165px;
    width: 370px;
    height: 620px;
    border-radius: 22px;
    background: var(--card-white);
    box-shadow: var(--shadow);
    overflow: hidden;
  }
  .card--back { left: 175px; }
  .card--front { left: 655px; }

  .brand { display: flex; align-items: center; gap: 10px; }
  .brand__square { width: 30px; height: 30px; background: var(--brand-blue); flex: none; }
  .brand__name {
    font-weight: 700;
    font-size: 30px;
    letter-spacing: 2px;
    color: var(--brand-blue);
    line-height: 1;
  }
  .card--back .brand {
    position: absolute;
    top: 270px;
    left: 50%;
    transform: translateX(-50%);
  }

  .social {
    position: absolute;
    right: 26px;
    bottom: 26px;
    display: flex;
    align-items: center;
    gap: 14px;
  }
  .social__label { font-size: 15px; letter-spacing: 1px; color: var(--ink); }
  .social__dot { width: 18px; height: 18px; border-radius: 50%; background: var(--ink); }

  .front__header { height: 240px; padding: 40px 34px 0; position: relative; }
  .licence {
    margin-top: 18px;
    font-size: 13px;
    line-height: 1.5;
    letter-spacing: 0.5px;
    color: var(--ink-soft);
  }
  .front__identity {
    position: absolute;
    left: 34px; right: 34px;
    top: 178px;
    display: flex;
    align-items: center;
    justify-content: space-between;
  }
  .person { display: flex; align-items: center; gap: 10px; }
  .person__name { font-size: 21px; letter-spacing: 2px; font-weight: 400; }
  .person__role { font-size: 19px; letter-spacing: 1.5px; }

  .contact-panel {
    position: absolute;
    top: 240px; left: 0; right: 0; bottom: 0;
    background: var(--brand-blue);
  }
  .contact-panel__accent {
    position: absolute;
    left: 0; top: 95px; bottom: 0;
    width: 38px;
    background: var(--brand-green);
  }
  .contact-list { list-style: none; }
  .contact-list__item {
    height: 95px;
    display: flex;
    align-items: center;
    gap: 18px;
    padding-left: 62px;
    padding-right: 16px;
    border-bottom: 1px solid var(--divider);
    color: #fff;
    font-size: 17px;
    letter-spacing: 0.6px;
    line-height: 1.3;
  }
  .contact-list__item:last-child { border-bottom: none; }
  .contact-list__icon { width: 24px; height: 24px; flex: none; fill: #fff; }
  .contact-list__sub { display: block; font-size: 13px; opacity: 0.85; letter-spacing: 0.4px; }
</style>
</head>
<body>

<section class="card card--back" aria-label="Card back">
  <div class="brand">
    <span class="brand__square"></span>
    <span class="brand__name">QLPN</span>
  </div>
  <div class="social" aria-label="Social links">
    <span class="social__label">like</span>
    <span class="social__dot"></span>
    <span class="social__dot"></span>
    <span class="social__dot"></span>
  </div>
</section>

<section class="card card--front" aria-label="Card front">
  <header class="front__header">
    <div class="brand">
      <span class="brand__square"></span>
      <span class="brand__name">QLPN</span>
    </div>
    <p class="licence">Australian Credit Licence: 782316</p>
    <div class="front__identity">
      <div class="person">
        <svg width="18" height="18" viewBox="0 0 24 24" aria-hidden="true"><circle cx="12" cy="7" r="5" fill="#2e2e2e"/><path d="M2 24c0-6 4.5-10 10-10s10 4 10 10z" fill="#2e2e2e"/></svg>
        <span class="person__name">LIAM CARTER</span>
      </div>
      <span class="person__role">founder</span>
    </div>
  </header>

  <div class="contact-panel">
    <div class="contact-panel__accent"></div>
    <ul class="contact-list">
      <li class="contact-list__item">
        <svg class="contact-list__icon" viewBox="0 0 24 24" aria-hidden="true"><path d="M6.6 10.8a15 15 0 006.6 6.6l2.2-2.2a1 1 0 011-.25 11.4 11.4 0 003.6.6 1 1 0 011 1V20a1 1 0 01-1 1A17 17 0 013 4a1 1 0 011-1h3.5a1 1 0 011 1c0 1.25.2 2.45.6 3.6a1 1 0 01-.25 1z"/></svg>
        <span>M 021 784 3902
          <span class="contact-list__sub">T 07 3184 2290 &nbsp;·&nbsp; F 07 3184 2291</span>
        </span>
      </li>
      <li class="contact-list__item">
        <svg class="contact-list__icon" viewBox="0 0 24 24" aria-hidden="true"><path d="M2 5h20v14H2z M3.5 6.5v.4l8.5 6 8.5-6v-.4z" fill-rule="evenodd"/></svg>
        <span>hello@harbourlend.com</span>
      </li>
      <li class="contact-list__item">
        <svg class="contact-list__icon" viewBox="0 0 24 24" aria-hidden="true"><circle cx="12" cy="12" r="10" fill="none" stroke="#fff" stroke-width="1.8"/><ellipse cx="12" cy="12" rx="4.5" ry="10" fill="none" stroke="#fff" stroke-width="1.6"/><path d="M2 12h20M4 7h16M4 17h16" stroke="#fff" stroke-width="1.4"/></svg>
        <span>www.harbourlend.com</span>
      </li>
      <li class="contact-list__item">
        <svg class="contact-list__icon" viewBox="0 0 24 24" aria-hidden="true"><path d="M12 1a8 8 0 00-8 8c0 6 8 14 8 14s8-8 8-14a8 8 0 00-8-8zm0 11a3 3 0 110-6 3 3 0 010 6z"/></svg>
        <span>41, 9th floor, Kestrel House<br>Bayview Road QLD</span>
      </li>
    </ul>
  </div>
</section>

</body>
</html>
```